BrivoLane Ute.

I want the full logo on one side. And the other side the card if right Ralf the logo the left half orange like the car in the logo color with Danielle R Morrow
Founder and CEO
Email symbol then dmorrow@brivolaneute.com
Www symbol. Then Brivolaneute.com
Phone symbol then 413-926-BRIV
The very bottom would like Brivo Lane Ute is a division of Harmond Vistas. LLC

```html
<!DOCTYPE html>
<html lang="en">
<head>
<meta charset="utf-8">
<title>BrivoLane Ute – Business Card</title>
<link href="https://fonts.googleapis.com/css2?family=Arimo:wght@400;700&display=swap" rel="stylesheet">
<style>
  :root {
    --bg: #2e2e2e;
    --card: #f7f7f7;
    --orange: #d9801f;
    --orange-dark: #b8661a;
    --ink: #141414;
    --logo-ink: #2b2b2b;
    --white: #ffffff;
  }
  * { box-sizing: border-box; margin: 0; padding: 0; }
  html, body {
    width: 1200px; height: 997px; overflow: hidden;
    background: var(--bg);
    font-family: "Arimo", Arial, sans-serif;
  }
  .stage { position: relative; width: 1200px; height: 997px; }
  .card {
    position: absolute;
    width: 520px; height: 297px;
    background: var(--card);
    border-radius: 4px 44px 4px 44px;
    overflow: hidden;
  }
  .card--front { left: 50px; top: 350px; }
  .card--back { left: 630px; top: 350px; }

  .logo {
    position: absolute;
    display: flex; align-items: center; gap: 12px;
    color: var(--logo-ink);
    font-weight: 700;
    white-space: nowrap;
    z-index: 1;
  }
  .logo__dot { border-radius: 50%; background: var(--orange); flex: none; }
  .card--front .logo { left: 50%; top: 50%; transform: translate(-50%, -50%); font-size: 44px; }
  .card--front .logo__dot { width: 52px; height: 52px; }
  .card--back .logo { left: 50%; top: 42px; transform: translateX(-50%); font-size: 26px; gap: 8px; }
  .card--back .logo__dot { width: 30px; height: 30px; }

  .swoosh { position: absolute; inset: 0; }

  .contact { position: absolute; left: 22px; top: 160px; color: var(--white); z-index: 1; }
  .contact__name { color: var(--ink); font-weight: 700; font-size: 15px; line-height: 18px; }
  .contact__title { font-size: 13px; line-height: 16px; margin-bottom: 8px; }
  .contact__row { display: flex; align-items: center; gap: 7px; font-size: 13px; line-height: 19px; }
  .contact__icon { width: 14px; height: 14px; flex: none; }

  .footer {
    position: absolute; right: 26px; bottom: 7px;
    font-size: 10.5px; color: var(--ink);
  }
  .footer__brand { color: var(--orange); font-weight: 700; }
</style>
</head>
<body>
<main class="stage">
  <section class="card card--front" aria-label="Card front">
    <div class="logo"><span class="logo__dot"></span>BrivoLane Ute</div>
  </section>

  <section class="card card--back" aria-label="Card back">
    <svg class="swoosh" viewBox="0 0 520 297" aria-hidden="true">
      <path d="M0,150 C140,128 300,170 520,92 L520,272 L0,272 Z" fill="var(--orange)"/>
      <path d="M0,150 C140,128 300,170 520,92 L520,98 C300,178 140,136 0,156 Z" fill="var(--orange-dark)"/>
      <path d="M0,148 C110,134 190,138 210,140 C140,136 60,142 0,154 Z" fill="var(--ink)"/>
      <path d="M200,126 C330,128 440,102 520,56 L520,84 C430,128 320,138 200,126 Z" fill="var(--ink)"/>
    </svg>
    <div class="logo"><span class="logo__dot"></span>BrivoLane Ute</div>
    <div class="contact">
      <p class="contact__name">Danielle R Morrow</p>
      <p class="contact__title">Founder &amp; CEO</p>
      <p class="contact__row">
        <svg class="contact__icon" viewBox="0 0 14 14" aria-hidden="true"><circle cx="7" cy="7" r="7" fill="#222"/><path d="M4,4.5 L5.5,4 L6.3,5.6 L5.5,6.3 C6,7.3 6.7,8 7.7,8.5 L8.4,7.7 L10,8.5 L9.5,10 C6.5,9.8 4.2,7.5 4,4.5 Z" fill="#fff"/></svg>
        413-926-BRIV
      </p>
      <p class="contact__row">
        <svg class="contact__icon" viewBox="0 0 14 14" aria-hidden="true"><circle cx="7" cy="7" r="7" fill="#222"/><rect x="3.5" y="4.5" width="7" height="5" fill="none" stroke="#fff" stroke-width="0.9"/><path d="M3.5,4.5 L7,7.3 L10.5,4.5" fill="none" stroke="#fff" stroke-width="0.9"/></svg>
        dmorrow@brivolaneute.com
      </p>
      <p class="contact__row">
        <svg class="contact__icon" viewBox="0 0 14 14" aria-hidden="true"><circle cx="7" cy="7" r="7" fill="#222"/><circle cx="7" cy="7" r="3.6" fill="none" stroke="#fff" stroke-width="0.9"/><path d="M3.4,7 H10.6 M7,3.4 C5.4,5.5 5.4,8.5 7,10.6 M7,3.4 C8.6,5.5 8.6,8.5 7,10.6" fill="none" stroke="#fff" stroke-width="0.8"/></svg>
        www.Brivolaneute.com
      </p>
    </div>
    <p class="footer"><span class="footer__brand">Brivo Lane Ute</span> is a division of Harmond Vistas. LLC</p>
  </section>
</main>
</body>
</html>
```